Brisk Hauling Stationary design

We need a new company logo for our stationary. Be creative. Most company apparel and hats are Navy blue and Light gray. Logo does not necessarily have to contain those two colors. Pictures of trees, logging equipment, log trucks, and logs are acceptable but not required. I am open to any and all designs. Logo must reflect our pride and professionalism in the East Texas Timber Industry.
Updates

Target Market(s)

Timber owners and sawmills. Adults 25 years and up

Industry/Entity Type

Industry

Font styles to use
Serif
Decorative

Requirements
Must have
• R. T. Brisk Hauling Co.
Nice to have
• Phone number: 555-555-0142
address:
PO Box 4810
Cedar Bend, TX 70000
www.rtbriskhauling.example
rtbriskhauling@mailbox.example

```html
<!DOCTYPE html>
<html lang="en">
<head>
<meta charset="utf-8">
<title>R. T. Brisk Hauling Co. — Envelope</title>
<link rel="stylesheet" href="https://fonts.googleapis.com/css2?family=Roboto+Slab:wght@400;700&display=swap">
<style>
  :root {
    --backdrop: #d9dadc;
    --paper: #ffffff;
    --flap-gray: #a9acb0;
    --navy: #1b2a4a;
    --ink-gray: #8a8c90;
  }
  * { box-sizing: border-box; margin: 0; padding: 0; }
  html, body {
    width: 1200px; height: 800px; overflow: hidden;
    background: var(--backdrop);
    font-family: "Roboto Slab", Georgia, serif;
  }
  .stationery {
    position: relative; width: 1200px; height: 800px;
    display: flex; align-items: center; justify-content: center; gap: 40px;
  }
  .envelope {
    position: relative; width: 540px; height: 270px;
    background: var(--paper);
    box-shadow: 0 6px 18px rgba(0,0,0,0.18);
    overflow: hidden;
  }
  .envelope__flap {
    position: absolute; inset: 0; width: 100%; height: 100%;
  }
  .brand {
    position: absolute;
    display: flex; align-items: center; gap: 10px;
    color: var(--navy);
    white-space: nowrap;
  }
  .brand__square {
    flex: none; width: 24px; height: 24px; background: var(--navy);
  }
  .brand__name {
    font-weight: 700; font-size: 19px; letter-spacing: 0.5px; line-height: 1;
    text-transform: uppercase;
  }
  .envelope--back .brand { left: 30px; top: 118px; }
  .envelope--front .brand { left: 30px; top: 32px; }
  .return-address {
    position: absolute; left: 30px; bottom: 28px;
    font-size: 10.5px; line-height: 1.4; color: var(--ink-gray);
    font-style: normal;
  }
</style>
</head>
<body>
<main class="stationery">
  <section class="envelope envelope--back" aria-label="Envelope back">
    <svg class="envelope__flap" viewBox="0 0 540 270" preserveAspectRatio="none" aria-hidden="true">
      <path d="M0 0 H340 C260 60 270 200 200 270 H0 Z" fill="var(--flap-gray)"/>
    </svg>
    <div class="brand">
      <span class="brand__square"></span>
      <span class="brand__name">R. T. Brisk Hauling Co.</span>
    </div>
  </section>

  <section class="envelope envelope--front" aria-label="Envelope front">
    <div class="brand">
      <span class="brand__square"></span>
      <span class="brand__name">R. T. Brisk Hauling Co.</span>
    </div>
    <address class="return-address">
      PO Box 4810<br>
      Cedar Bend, TX 70000<br>
      www.rtbriskhauling.example<br>
      rtbriskhauling@mailbox.example<br>
      Phone: 555-555-0142
    </address>
  </section>
</main>
</body>
</html>
```